Post Card Mailer for QUIK PATH PROSPECTS using new logo

We need a post card designed to send through the USA mail service that will go to new prospective clients.

The post card will introduce me and my new company and try to educate them our on company and services.

The goal is for them to call me or email me so I can have a discussion and try to sell our product.

Our product is a name list of individuals that are looking for consulting / help to determine if they qualify for USA social security benefits and then help to manage the process. We sell this name list to law firms that help these individuals.

Our services are better because we have a better less expensive way to identify people via the internet that want help. Our conversion rate is 15%, so every 100 leads a law firm buys the will obtain 15 customers / clients.

Designer on Logo took alot longer than expected. Also there were two projects that needed to combined into one. Which was done yesterday.

Target Market(s)

Law firms

Font styles to use
Serif
Sans Serif
Script

Colors

Designer to choose colors to be used in the design.

Requirements
Must have
• The size of the mailer should be about 6 by 8 inches.
• Two sides.
• Side 1: With our Logo and key messages we want to communicate.
• Side 2: A space to be used by the USA mail services in lower right, my photo and an introduction by me to our company and why they should buy from my company.
Nice to have
• Images that represent what we do, how we help, and our target market.
Should not have
• Poor taste in images that upset people

```html
<!DOCTYPE html>
<html lang="en">
<head>
<meta charset="utf-8">
<title>Quik Path Prospects – Postcard Mailer</title>
<link rel="stylesheet" href="https://fonts.googleapis.com/css2?family=Montserrat:ital,wght@0,500;0,700;0,800;1,500;1,700&family=Roboto+Condensed:wght@400;700&family=Arimo:wght@400;700&display=swap">
<style>
  :root{
    --page:#d6d6d6;
    --navy:#1d2530;
    --navy-2:#2b3645;
    --blue:#1f6fd6;
    --blue-deep:#0f56b8;
    --brand:#2a8fe6;
    --cyan:#21c4f0;
    --ink:#2d3440;
    --head-blue:#1668b8;
    --white:#ffffff;
  }
  *{box-sizing:border-box;margin:0;padding:0}
  html,body{width:1200px;height:1200px;overflow:hidden;background:var(--page)}
  body{position:relative;font-family:"Roboto Condensed",sans-serif}

  .card{position:absolute;left:281px;width:676px;overflow:hidden}

  /* ---------- front ---------- */
  .front{top:90px;height:508px;background:var(--navy)}
  .front-hero{position:absolute;left:0;top:0;width:676px;height:320px;
    background:linear-gradient(120deg,#1a2230 0%,#2a3646 55%,#3a4554 100%)}
  .hero-art{position:absolute;left:20px;top:10px;width:390px;height:300px;border-radius:50%;
    background:radial-gradient(ellipse at 50% 45%,#8fd8ff 0%,#3b8fd0 30%,rgba(40,80,130,.55) 58%,rgba(30,40,55,0) 75%)}
  .front-logo{position:absolute;right:20px;top:70px;width:236px;text-align:left;
    font-family:"Montserrat",sans-serif;font-weight:800;font-size:36px;line-height:1.02;color:var(--brand);letter-spacing:.5px}

  .features{position:absolute;left:0;top:320px;width:676px;height:188px;
    background:linear-gradient(180deg,var(--blue) 0%,var(--blue-deep) 100%);display:flex}
  .feature{flex:1;position:relative;padding:40px 8px 0;text-align:center;color:var(--white);
    border-right:1px solid rgba(255,255,255,.12)}
  .feature:last-child{border-right:none}
  .feature-icon{position:absolute;left:50%;top:-40px;width:68px;height:68px;margin-left:-34px;border-radius:50%;
    background:var(--blue-deep);box-shadow:0 0 0 3px rgba(33,196,240,.35)}
  .feature-icon svg{width:68px;height:68px}
  .feature h3{font-family:"Montserrat",sans-serif;font-weight:800;font-size:14.5px;line-height:.98;margin-bottom:8px;text-transform:uppercase}
  .feature p{font-size:12.6px;line-height:1.12;margin-bottom:4px}

  .web-tab{position:absolute;left:192px;top:464px;width:292px;height:44px;background:var(--navy);
    clip-path:polygon(3% 0,97% 0,100% 100%,0 100%);
    font-family:"Montserrat",sans-serif;font-size:21px;font-weight:500;color:var(--white);
    text-align:center;line-height:46px}
  .web-tab b{font-weight:700}
  .front-stripe{position:absolute;left:0;bottom:0;width:676px;height:4px;background:var(--cyan)}

  /* ---------- back ---------- */
  .back{top:618px;height:504px;background:linear-gradient(180deg,#fff 0%,#fff 70%,#f1f2f4 100%)}
  .portrait{position:absolute;left:19px;top:10px;width:128px;height:128px;border-radius:50%;
    border:3px solid var(--cyan);background:linear-gradient(160deg,#c9ccd2 0%,#8c929c 100%)}
  .portrait-caption{position:absolute;left:0;top:142px;width:166px;text-align:center;
    font-family:"Montserrat",sans-serif;color:var(--head-blue);font-size:10px;line-height:1.3}
  .portrait-caption strong{font-weight:700;font-style:italic;font-size:10.5px}
  .portrait-caption em{font-weight:500}
  .back-logo{position:absolute;left:159px;top:50px;width:180px;
    font-family:"Montserrat",sans-serif;font-weight:800;font-size:24px;line-height:1.05;color:var(--brand)}

  .pitch{position:absolute;left:355px;top:0;width:321px;height:136px;background:var(--navy);
    clip-path:polygon(5px 0,100% 0,100% 100%,0 100%);
    padding:36px 8px 0 22px;font-family:"Arimo",sans-serif;color:var(--white);
    font-size:18px;line-height:.9;text-transform:uppercase}
  .pitch b{font-weight:700}
  .pitch span{font-weight:400;display:inline-block;margin-top:2px}

  .test-band{position:absolute;left:299px;top:136px;width:377px;height:78px;
    background:linear-gradient(90deg,#0d63b0 0%,#1b8fd6 100%);
    clip-path:polygon(0 0,100% 0,100% 100%,4% 100%);color:var(--white);padding:8px 0 0 24px}
  .test-band h2{font-family:"Montserrat",sans-serif;font-weight:800;font-size:20px;letter-spacing:.2px;margin-bottom:6px}
  .test-steps{display:flex;font-weight:700;font-size:12px;line-height:1.15}
  .test-steps div{padding:0 6px;border-left:1.5px solid var(--white)}
  .test-steps div:first-child{padding-left:0;border-left:none}

  .intro{position:absolute;left:28px;top:182px;width:252px;color:var(--ink)}
  .intro h2{font-family:"Montserrat",sans-serif;font-weight:700;font-size:14px;line-height:1.2;color:var(--head-blue);margin-bottom:8px}
  .intro ul{list-style:none}
  .intro li{position:relative;padding-left:16px;font-family:"Arimo",sans-serif;font-size:9.6px;line-height:1.3;margin-bottom:6px}
  .intro li::before{content:"";position:absolute;left:0;top:4px;width:4px;height:4px;border-radius:50%;background:var(--head-blue)}
  .closing{position:absolute;left:26px;top:425px;width:256px;height:58px;
    border-top:2px solid var(--head-blue);border-bottom:2px solid var(--head-blue);
    padding:7px 10px 0;font-weight:700;font-size:11.3px;line-height:1.25;color:var(--head-blue);text-transform:uppercase}

  .return-address{position:absolute;left:351px;top:256px;width:190px;font-style:normal;
    font-family:"Arimo",sans-serif;font-size:10.2px;line-height:1.27;color:var(--ink)}
  .stamp-box{position:absolute;left:555px;top:245px;width:94px;height:94px;border:1px solid #555}
  .addressee{position:absolute;left:353px;top:378px;font-family:"Arimo",sans-serif;font-weight:700;font-size:10.2px;line-height:1.3;color:#111}
</style>
</head>
<body>

<section class="card front" aria-label="Postcard front">
  <div class="front-hero">
    <div class="hero-art" role="img" aria-label="Open hand holding a glowing network of laptop, phone and connected digital icons"></div>
    <div class="front-logo">QUIK PATH PROSPECTS</div>
  </div>

  <div class="features">
    <div class="feature">
      <div class="feature-icon"><svg viewBox="0 0 68 68"><polygon points="34,16 39,29 53,29 42,37 46,51 34,43 22,51 26,37 15,29 29,29" fill="#62b7ff" stroke="#0b1f3a" stroke-width="1.6"/></svg></div>
      <h3>Best Leads,<br>Best Price</h3>
      <p>• Our high conversation rates lowers your client acquisition cost</p>
      <p>• Referrals available</p>
    </div>
    <div class="feature">
      <div class="feature-icon"><svg viewBox="0 0 68 68"><rect x="18" y="32" width="8" height="16" fill="#dfe7f2"/><path d="M28 48V32l7-12c3 0 4 2 3 6l-1 4h10c3 0 4 3 3 5l-3 11c-1 2-2 2-4 2z" fill="#62b7ff" stroke="#0b1f3a" stroke-width="1.4"/></svg></div>
      <h3>Trusted<br>Partner</h3>
      <p>• Reliability, Dependable, Helpful</p>
      <p>• Deep business &amp; process acumen</p>
    </div>
    <div class="feature">
      <div class="feature-icon"><svg viewBox="0 0 68 68"><path d="M24 40l-5 14 7-3 4 5 4-11z M44 40l5 14-7-3-4 5-4-11z" fill="#2a2f38"/><circle cx="34" cy="30" r="14" fill="#62b7ff" stroke="#0b1f3a" stroke-width="1.6"/><polygon points="34,23 36,28 41,28 37,31 39,36 34,33 29,36 31,31 27,28 32,28" fill="#0b1f3a"/></svg></div>
      <h3>High Volume,<br>Quality Leads</h3>
      <p>• 50 years of SSD domain knowledge</p>
      <p>• Tested technology capabilities</p>
    </div>
    <div class="feature">
      <div class="feature-icon"><svg viewBox="0 0 68 68" fill="none" stroke="#0b1f3a" stroke-width="1.6"><path d="M22 26L34 18 46 26 46 42 34 50 22 42z M22 26L46 42 M46 26L22 42 M34 18V50"/><g fill="#62b7ff"><circle cx="34" cy="18" r="3.5"/><circle cx="46" cy="26" r="3.5"/><circle cx="46" cy="42" r="3.5"/><circle cx="34" cy="50" r="3.5"/><circle cx="22" cy="42" r="3.5"/><circle cx="22" cy="26" r="3.5"/><circle cx="34" cy="34" r="3.5"/></g></svg></div>
      <h3>EZ To Us</h3>
      <p>• Integrate seamlessly into your IT systems</p>
      <p>• Tailored campaigns</p>
    </div>
  </div>

  <div class="web-tab"><b>QuikPathProspects</b>.com</div>
  <div class="front-stripe"></div>
</section>

<section class="card back" aria-label="Postcard back">
  <div class="portrait" role="img" aria-label="Portrait photo of the company president"></div>
  <div class="portrait-caption"><strong>Marcus Ellwood</strong><br><em>President, Quik Path Prospects</em></div>
  <div class="back-logo">QUIK PATH PROSPECTS</div>

  <div class="pitch">
    <b>Best Leads … Best Price<br>with High Volume &amp; Quality<br>Capacity …</b><br>
    <span>Leads from a trusted<br>partner that is EZ to use</span>
  </div>

  <div class="test-band">
    <h2>TEST OUR LEADS</h2>
    <div class="test-steps">
      <div>Start at 250<br>or 500 Leads.</div>
      <div>Grow to 1,000 …<br>3,000 or even 10,000!</div>
      <div>We give the right<br>support to your growth.</div>
    </div>
  </div>

  <div class="intro">
    <h2>I want to personally introduce our company to you!</h2>
    <ul>
      <li>My team as &gt; 50 years of cumulative SSD experience.</li>
      <li>We have proven technology that delivers the best leads.</li>
      <li>The timing is right for a new competitor in this industry.</li>
      <li>I had to come out of retirement after 30 years with Norvale Industries, the opportunity is just that great … I love building businesses and partnering with great customers!</li>
      <li>Our business, industry, &amp; technical acumen is unrivaled … and we can do it at a cost than no others can.</li>
    </ul>
  </div>

  <div class="closing">Let’s work together to bring social security disability benefits to those in need and deserving!</div>

  <address class="return-address">
    Marcus Ellwood, President<br>
    Quik Path Prospects<br>
    2150 Harlow Avenue, Suite 400<br>
    Dayton Ohio OH 45402<br>
    555-014-2288<br>
    Marcus@QuikPathProspects.com
  </address>
  <div class="stamp-box" aria-label="Postage area"></div>
  <div class="addressee">To:&nbsp; Addressee</div>
</section>

</body>
</html>
```